Business Card Design

I'm a young beekeeper (22 years old) just starting out. I own and run 80 hives and would like to eventually build up to 1000. My aim is to run it in tandem with our family farm that is currently running sheep and beef. Unlike a number of honey companies on the East Coast (or the North Island, NZ) I am local and will expand onto the lease blocks that our family is also leasing. I want a simple plain logo/photo. The designer may wish to use one of the photos as a background outline or however they chose. The mountain is Aorangi and our farm borders one side of it.

Target Market(s)

From local land owners to wholesale honey buyers

Industry/Entity Type

Farm

Contact Information for Business Card

Pekeriu Honey
Manager Owner Manaia Brooks
email pekeriuhoney@tuimailbox.co.nz
mobile 0217394461

Requirements
Must have
• The details submitted. The brand Pekeriu Honey to be the main feature. The other details can be smaller.
Should not have
• Must not include a picture of a bee or hive. Use a modern font. Don't use koru but may incorporate poutama.

```html
<!DOCTYPE html>
<html lang="en">
<head>
<meta charset="utf-8">
<title>Pekeriu Honey – Business Card</title>
<link rel="stylesheet" href="https://fonts.googleapis.com/css2?family=Open+Sans:wght@400;700&display=swap">
<style>
  :root {
    --page-bg: #f4f4f2;
    --sky-top: #c9d3db;
    --sky-low: #e6e9ea;
    --mountain: #3b3a36;
    --mountain-dark: #2a2925;
    --ground: #6e5a3c;
    --ground-light: #9a7e55;
    --band: rgba(12, 12, 10, 0.82);
    --accent-yellow: #f3d200;
    --text-light: #ffffff;
  }
  html, body {
    margin: 0;
    width: 1200px;
    height: 900px;
    overflow: hidden;
    background: var(--page-bg);
    font-family: "Open Sans", "Segoe UI", sans-serif;
  }
  .business-card {
    position: absolute;
    left: 75px;
    top: 150px;
    width: 1050px;
    height: 600px;
    border-radius: 40px;
    overflow: hidden;
    box-shadow: 0 12px 30px rgba(0, 0, 0, 0.18);
  }
  .landscape-photo {
    position: absolute;
    inset: 0;
    background:
      linear-gradient(180deg,
        var(--sky-top) 0%,
        var(--sky-low) 30%,
        var(--mountain) 40%,
        var(--mountain-dark) 62%,
        #3a3326 78%,
        var(--ground) 90%,
        var(--ground-light) 100%);
  }
  .brand-name {
    position: absolute;
    top: 62px;
    left: 0;
    right: 0;
    margin: 0;
    text-align: center;
    font-weight: 700;
    font-size: 82px;
    letter-spacing: 8px;
    text-transform: uppercase;
    color: var(--accent-yellow);
  }
  .contact-band {
    position: absolute;
    left: 0;
    right: 0;
    top: 372px;
    height: 168px;
    background: var(--band);
    border-top: 3px solid var(--accent-yellow);
    border-bottom: 3px solid var(--accent-yellow);
    text-align: center;
    color: var(--text-light);
  }
  .person-name {
    margin: 14px 0 0;
    font-weight: 700;
    font-size: 30px;
    line-height: 1.2;
    color: var(--accent-yellow);
  }
  .person-role {
    margin: 2px 0 0;
    font-size: 19px;
    line-height: 1.2;
  }
  .contact-phone {
    margin: 16px 0 0;
    font-size: 30px;
    line-height: 1.2;
  }
  .contact-email {
    margin: 2px 0 0;
    font-size: 24px;
    line-height: 1.2;
  }
</style>
</head>
<body>
  <main class="business-card">
    <div class="landscape-photo" role="img" aria-label="Photograph of the mountain rising above farmland under a pale sky"></div>
    <h1 class="brand-name">Pekeriu Honey</h1>
    <section class="contact-band">
      <p class="person-name">Manaia Brooks</p>
      <p class="person-role">Manager Owner</p>
      <p class="contact-phone">0217394461</p>
      <p class="contact-email">pekeriuhoney@tuimailbox.co.nz</p>
    </section>
  </main>
</body>
</html>
```